Harbor Line Tech Service, Technology & Security Co.

need a new business card design for our Technology & Security Company. We are a Computer Networking Company, Security Camera Installers, Phone Systems.

Target Market(s)

Construction, Medical, Law Offices, Accounting, Retail etc.

Industry/Entity Type

Information Technology

Logo is attached, colors are Blue, Red, Black. Blue for Technology & Red is for Security Cameras, Access Control, Alarm Systems

Colors
fbed22
ec1f27
0555a3
ffffff

Requirements
Must have
• Pictures or Icons for
• For Technology:
• Computer, Network, Phone System, Copier, TV, Cabling
• For Security:
• Video Surveillance, Access Control, Intercom, Fire Alarm, Burglar Alarm, Time Clock

```html
<!DOCTYPE html>
<html lang="en">
<head>
<meta charset="utf-8">
<title>Harbor Line Tech Service – Business Card</title>
<link href="https://fonts.googleapis.com/css2?family=Open+Sans:wght@400;600;700;800&display=swap" rel="stylesheet">
<style>
  :root{
    --bg:#3b3634;
    --card:#141414;
    --card-edge:#1d1d1d;
    --white:#ffffff;
    --grey:#cfcfcf;
    --blue-light:#2f86d6;
    --red:#ec1f27;
    --divider:#5a5a5a;
  }
  *{margin:0;padding:0;box-sizing:border-box}
  html,body{width:1200px;height:864px;overflow:hidden;background:var(--bg)}
  body{position:relative;font-family:"Open Sans",Arial,sans-serif;color:var(--white)}

  .card{
    position:absolute;width:540px;height:309px;border-radius:4px;
    background:linear-gradient(160deg,var(--card-edge),var(--card) 60%);
    box-shadow:0 18px 40px rgba(0,0,0,.45);
  }
  .card--front{left:60px;top:110px}
  .card--back{left:600px;top:440px}

  /* front */
  .brand{position:absolute;left:0;right:0;top:44px;text-align:center}
  .brand__name{font-size:26px;font-weight:700;letter-spacing:.5px;color:var(--grey);line-height:1.2}
  .brand__tagline{margin-top:6px;font-size:14px;font-weight:400;color:var(--grey);letter-spacing:.3px}

  .services{position:absolute;left:0;right:0;top:134px;text-align:center}
  .services__heading{font-size:13px;font-weight:700;letter-spacing:.5px;margin-top:8px}
  .services__heading--tech{color:var(--blue-light)}
  .services__heading--sec{color:var(--red)}
  .services__list{font-size:13.5px;color:var(--grey);line-height:1.35}
  .dot{display:inline-block;width:4px;height:4px;border-radius:50%;margin:0 6px;vertical-align:middle}
  .dot--blue{background:var(--blue-light)}
  .dot--red{background:var(--red)}

  /* back */
  .mark{position:absolute;left:40px;top:120px;width:200px;display:flex;align-items:center;gap:10px}
  .mark__circle{width:16px;height:16px;border-radius:50%;background:var(--red);flex:none}
  .mark__name{font-size:18px;font-weight:700;color:var(--white);line-height:1.2}
  .divider{position:absolute;left:262px;top:70px;width:1px;height:170px;background:linear-gradient(var(--card),var(--divider),var(--card))}

  .contact{position:absolute;left:290px;top:72px}
  .contact__name{font-size:15px;font-weight:700;color:var(--blue-light);letter-spacing:.3px}
  .contact__title{font-size:15px;font-weight:600;color:var(--red);margin-bottom:6px}
  .contact__address{font-size:14px;line-height:1.3;color:var(--white)}
  .contact__lines{list-style:none;margin-top:4px}
  .contact__lines li{display:flex;align-items:center;gap:8px;font-size:14px;line-height:1.45}
  .contact__lines svg{width:12px;height:12px;fill:var(--blue-light);flex:none}
  .contact__lines .no-icon{padding-left:20px}
</style>
</head>
<body>

<section class="card card--front" aria-label="Card front">
  <div class="brand">
    <div class="brand__name">HARBOR LINE TECH SERVICE</div>
    <div class="brand__tagline">Technology &amp; Security Co.</div>
  </div>
  <div class="services">
    <div class="services__heading services__heading--tech">FOR TECHNOLOGY</div>
    <div class="services__list">Computer<i class="dot dot--blue"></i>Network<i class="dot dot--blue"></i>Phone System</div>
    <div class="services__list">Copier<i class="dot dot--blue"></i>TV<i class="dot dot--blue"></i>Cabling</div>
    <div class="services__heading services__heading--sec">FOR SECURITY</div>
    <div class="services__list">Video Surveillance<i class="dot dot--red"></i>Access Control<i class="dot dot--red"></i>Intercom</div>
    <div class="services__list">Fire Alarm<i class="dot dot--red"></i>Burglar Alarm<i class="dot dot--red"></i>Time Clock</div>
  </div>
</section>

<section class="card card--back" aria-label="Card back">
  <div class="mark">
    <span class="mark__circle"></span>
    <span class="mark__name">Harbor Line Tech Service</span>
  </div>
  <div class="divider"></div>
  <div class="contact">
    <div class="contact__name">DANIEL REYES</div>
    <div class="contact__title">CEO/FOUNDER</div>
    <div class="contact__address">2140 Alder Court<br>Juneau, Alaska 99801</div>
    <ul class="contact__lines">
      <li><svg viewBox="0 0 12 12"><path d="M1 3c0-1 1-2 2-2h6c1 0 2 1 2 2v1H8V3H4v1H1zM2 5h8l1 6H1z"/></svg>555 204 1187</li>
      <li><svg viewBox="0 0 12 12"><path d="M3 0h6v12H3zM4 1v8h4V1z"/></svg>555 318 4620</li>
      <li><svg viewBox="0 0 12 12"><path d="M3 0h6v4H3zM1 5h10v6H1zM3 7v2h6V7z"/></svg>555 472 9035</li>
      <li><svg viewBox="0 0 12 12"><circle cx="6" cy="6" r="5.5"/></svg>daniel@HarborLineTech.com</li>
      <li class="no-icon">www.HarborLineTech.com</li>
    </ul>
  </div>
</section>

</body>
</html>
```